New boutique IT consultancy needs business card

I need a business card and logo for my IT consultancy business, called 'Quenbrylle' . I want it to make me look bigger than I am. I want it to look classy, and modern. Simple design, that will be easy for me to translate into my webpage etc. The business card should be bold, and different.

The logo should emphasise the 'y' as used in quenbrylle

Target Market(s)

IT divisions in other companies

Industry/Entity Type

Business

Contact Information for Business Card

Marcel Thornby
Director
+61 437 819 063
mthornby@quenbrylle-mail.com

```html
<!DOCTYPE html>
<html lang="en">
<head>
<meta charset="utf-8">
<title>Quenbrylle — Business Card</title>
<link rel="stylesheet" href="https://fonts.googleapis.com/css2?family=Roboto:wght@400;500;700&display=swap">
<style>
  :root {
    --backdrop: #303032;
    --card: #2a2a2b;
    --card-edge: #202021;
    --ink-white: #f2f2f2;
    --accent-lime: #8cc63f;
    --accent-yellow: #d9e021;
    --faint-circle: rgba(255, 255, 255, 0.06);
  }
  * { box-sizing: border-box; margin: 0; padding: 0; }
  html, body {
    width: 900px;
    height: 1200px;
    overflow: hidden;
    background: var(--backdrop);
    font-family: "Roboto", Arial, sans-serif;
  }
  .canvas {
    position: relative;
    width: 900px;
    height: 1200px;
  }
  .card {
    position: absolute;
    left: 190px;
    width: 520px;
    height: 300px;
    background: var(--card);
    border-radius: 4px;
    box-shadow: 0 0 0 1px var(--card-edge);
    overflow: hidden;
  }
  .card--front { top: 150px; }
  .card--back { top: 750px; }

  .wordmark {
    position: absolute;
    left: 0;
    right: 0;
    text-align: center;
  }
  .wordmark__name {
    color: var(--ink-white);
    font-weight: 700;
    font-size: 28px;
    letter-spacing: 3px;
    line-height: 1;
  }
  .wordmark__tagline {
    margin-top: 6px;
    color: var(--accent-lime);
    font-weight: 400;
    font-size: 10px;
    letter-spacing: 7px;
    text-transform: uppercase;
  }

  .card--front .faint-circle {
    position: absolute;
    left: 160px;
    top: 50px;
    width: 200px;
    height: 200px;
    border-radius: 50%;
    background: var(--faint-circle);
  }
  .card--front .wordmark { top: 128px; }

  .card--back .brand-dot {
    position: absolute;
    left: 234px;
    top: 40px;
    width: 52px;
    height: 52px;
    border-radius: 50%;
    background: var(--accent-lime);
  }
  .card--back .wordmark { top: 108px; }

  .contact {
    position: absolute;
    right: 36px;
    top: 176px;
    list-style: none;
    color: var(--ink-white);
    font-size: 11px;
    line-height: 18px;
  }
  .contact__item { display: flex; align-items: center; gap: 6px; }
  .contact__icon { width: 11px; height: 11px; flex: none; }

  .person {
    position: absolute;
    left: 36px;
    bottom: 36px;
  }
  .person__name {
    color: var(--ink-white);
    font-weight: 500;
    font-size: 14px;
    letter-spacing: 1px;
    text-transform: uppercase;
  }
  .person__role {
    margin-top: 3px;
    color: var(--accent-yellow);
    font-weight: 500;
    font-size: 11px;
  }
</style>
</head>
<body>
<main class="canvas">

  <section class="card card--front" aria-label="Card front">
    <div class="faint-circle"></div>
    <div class="wordmark">
      <div class="wordmark__name">QUENBRYLLE</div>
      <div class="wordmark__tagline">Built to be clear</div>
    </div>
  </section>

  <section class="card card--back" aria-label="Card back">
    <div class="brand-dot"></div>
    <div class="wordmark">
      <div class="wordmark__name">QUENBRYLLE</div>
      <div class="wordmark__tagline">Built to be clear</div>
    </div>

    <ul class="contact">
      <li class="contact__item">
        <svg class="contact__icon" viewBox="0 0 12 12" aria-hidden="true">
          <rect width="12" height="12" rx="1.5" fill="var(--accent-yellow)"/>
          <path d="M3.4 2.6l1.3 1.6-.7.9c.5 1 1.2 1.7 2.2 2.2l.9-.7 1.6 1.3-.8 1.3C5.6 9 3 6.4 2.8 3.3z" fill="var(--card)"/>
        </svg>
        <span>+61 437 819 063</span>
      </li>
      <li class="contact__item">
        <svg class="contact__icon" viewBox="0 0 12 12" aria-hidden="true">
          <rect width="12" height="12" rx="1.5" fill="var(--accent-yellow)"/>
          <rect x="2.3" y="3.4" width="7.4" height="5.2" fill="none" stroke="var(--card)" stroke-width="1"/>
          <path d="M2.5 3.6L6 6.4l3.5-2.8" fill="none" stroke="var(--card)" stroke-width="1"/>
        </svg>
        <span>mthornby@quenbrylle-mail.com</span>
      </li>
    </ul>

    <div class="person">
      <div class="person__name">Marcel Thornby</div>
      <div class="person__role">Director</div>
    </div>
  </section>

</main>
</body>
</html>
```